Postcard Design

Law office.
Details are on the attached pdf file:
NOTE: the following items are to be changed, as follows:
1. price is 799
2. delete "Expires 2-8-13"
3. make "Nevada County's..." into "Northern California's ... "
4. Someplace where it fits nicely, add "Fast, Easy, Done!"
5. Delete "no obligation first visit"
6. That attached pdf was a successful ad so I want to maintain that look GENERALLY, but I'm not stuck on anything in particular. Some freedom to play with it for a perfect ad.
7. I'll attach the revised picture and the logo.

```html
<!DOCTYPE html>
<html lang="en">
<head>
<meta charset="utf-8">
<title>Estate Plans Postcard</title>
<link rel="stylesheet" href="https://fonts.googleapis.com/css2?family=Questrial&family=Crimson+Pro:ital,wght@0,400;0,600;0,700;1,700&family=Cormorant+Garamond:wght@500&display=swap">
<style>
  :root {
    --page: #e9e9ea;
    --card-edge: #ffffff;
    --frame: #1b1612;
    --ink: #141414;
    --ink-soft: #2a2a2a;
    --panel: rgba(246, 244, 241, 0.86);
    --banner: rgba(250, 250, 250, 0.92);
    --gold: #c9a35a;
    --warm-dark: #3b2d22;
    --warm-mid: #8d7658;
    --warm-light: #e8dcc7;
  }
  * { box-sizing: border-box; margin: 0; padding: 0; }
  html, body { width: 1200px; height: 900px; overflow: hidden; background: var(--page); }
  .postcard {
    position: absolute; left: 50px; top: 134px; width: 1100px; height: 632px;
    background: var(--card-edge); padding: 12px;
    box-shadow: 0 4px 14px rgba(0,0,0,0.18);
  }
  .postcard__frame {
    position: relative; width: 100%; height: 100%; overflow: hidden;
    background: var(--frame);
  }
  .backdrop {
    position: absolute; inset: 6px;
    background:
      linear-gradient(180deg, rgba(201,163,90,0.55) 0%, rgba(0,0,0,0) 18%),
      linear-gradient(100deg, var(--warm-dark) 0%, var(--warm-mid) 28%, var(--warm-light) 55%, #cfc3b2 75%, #6f5f50 100%);
  }
  .portrait {
    position: absolute; left: 40px; top: 40px; width: 440px; height: 500px;
    background: radial-gradient(ellipse at 50% 30%, #b98d6f 0%, #6b5140 22%, #1a1a1c 48%, #121214 100%);
    border-radius: 4px;
    opacity: 0.92;
  }
  .corner-mark {
    position: absolute; left: 16px; top: 14px; width: 36px; height: 36px;
    border: 2px solid var(--gold);
  }
  .offer-panel {
    position: absolute; left: 452px; top: 14px; right: 14px; bottom: 22px;
    background: var(--panel);
    text-align: center; color: var(--ink);
  }
  .offer-panel__headline {
    font-family: "Questrial", sans-serif; font-size: 35px; line-height: 40px;
    margin-top: 18px; letter-spacing: 0.5px;
  }
  .offer-panel__services {
    font-family: "Crimson Pro", serif; font-size: 19px; margin-top: 4px; color: var(--ink-soft);
  }
  .offer-panel__tagline {
    font-family: "Crimson Pro", serif; font-weight: 700; font-size: 30px; margin-top: 14px;
  }
  .offer-panel__price {
    font-family: "Crimson Pro", serif; font-style: italic; font-weight: 700; font-size: 42px;
    line-height: 44px; margin-top: 8px;
  }
  .offer-panel__value { font-family: "Crimson Pro", serif; font-size: 16px; }
  .offer-panel__slogan {
    font-family: "Crimson Pro", serif; font-style: italic; font-weight: 700; font-size: 50px;
    line-height: 54px; margin-top: 10px;
  }
  .offer-panel__cta {
    font-family: "Crimson Pro", serif; font-weight: 700; font-size: 25px; margin-top: 14px;
  }
  .offer-panel__phone {
    font-family: "Crimson Pro", serif; font-weight: 700; font-size: 34px; margin-top: 4px;
    display: flex; align-items: center; justify-content: center; gap: 14px; margin-right: 80px;
  }
  .offer-panel__phone svg { width: 22px; height: 22px; }
  .contact {
    position: absolute; left: 36px; top: 486px; text-align: left;
    font-family: "Crimson Pro", serif; font-weight: 700; color: var(--ink);
  }
  .contact__label { font-size: 19px; }
  .contact__web {
    display: flex; align-items: center; gap: 10px; font-size: 21px; margin: 6px 0 0 56px;
  }
  .contact__web svg { width: 17px; height: 17px; }
  .contact__note { font-size: 13px; font-weight: 400; margin: 16px 0 0 120px; }
  .firm-seal {
    position: absolute; right: 14px; bottom: 10px; width: 108px; text-align: center;
    font-family: "Crimson Pro", serif; color: var(--ink);
  }
  .firm-seal__box {
    width: 92px; height: 84px; margin: 0 auto; border: 2px solid var(--ink);
    display: flex; align-items: center; justify-content: center;
    font-family: "Cormorant Garamond", serif; font-size: 18px; background: #fff;
  }
  .firm-seal__caption { font-size: 14px; line-height: 16px; margin-top: 4px; }
  .name-banner {
    position: absolute; left: 28px; top: 500px; width: 456px; height: 96px;
    background: var(--banner);
    font-family: "Cormorant Garamond", serif; color: var(--ink);
  }
  .name-banner__prefix { position: absolute; left: 110px; top: 8px; font-size: 22px; }
  .name-banner__name { position: absolute; left: 18px; top: 30px; font-size: 50px; line-height: 58px; white-space: nowrap; }
</style>
</head>
<body>
  <section class="postcard">
    <div class="postcard__frame">
      <div class="backdrop" role="img" aria-label="Soft blurred office background in warm gold and cream tones"></div>
      <div class="portrait" role="img" aria-label="Portrait photo of the attorney in a dark suit and tie"></div>
      <div class="corner-mark"></div>

      <div class="offer-panel">
        <h1 class="offer-panel__headline">Northern California's<br>Best in Estate Plans</h1>
        <p class="offer-panel__services">Living Trusts, Wills &amp; All Necessary Documents</p>
        <p class="offer-panel__tagline">Protect Your Loved Ones!</p>
        <p class="offer-panel__price">$799</p>
        <p class="offer-panel__value">Over $2,000 value</p>
        <p class="offer-panel__slogan">Fast, Easy, Done!</p>
        <p class="offer-panel__cta">It’s Easy - Call Now!</p>
        <p class="offer-panel__phone">
          <svg viewBox="0 0 24 24" aria-hidden="true"><path fill="currentColor" d="M6.6 2.5l3 3.2-1.9 2.6c1.3 2.8 3.3 4.8 6 6.1l2.6-1.9 3.2 3-2 3.8C10.7 18.7 5.3 13.3 2.8 4.5z"/></svg>
          555-0142
        </p>
        <div class="contact">
          <p class="contact__label">Check me out at :</p>
          <p class="contact__web">
            <svg viewBox="0 0 24 24" aria-hidden="true"><g fill="none" stroke="currentColor" stroke-width="2"><circle cx="12" cy="12" r="10"/><ellipse cx="12" cy="12" rx="4.5" ry="10"/><path d="M2 12h20M4 6.5h16M4 17.5h16"/></g></svg>
            www.DanielMoreland.com
          </p>
          <p class="contact__note">• Free Notarization</p>
        </div>
        <div class="firm-seal">
          <div class="firm-seal__box">Moreland</div>
          <p class="firm-seal__caption">Thousands Served<br>Since 1998</p>
        </div>
      </div>

      <div class="name-banner">
        <span class="name-banner__prefix">Law Office Of</span>
        <span class="name-banner__name">Daniel R. Moreland</span>
      </div>
    </div>
  </section>
</body>
</html>
```